New Business Card Design Project

Details for my new Business Card Design Project will be added soon. Like a nice simple design

Target Market(s)

Home improvement

Industry/Entity Type

Home Improvement

Contact Information for Business Card

Roofing siding gutters additions garages decks

Requirements
Must have
• Phone 5074629183
• Email morvantgc@quellmail.com

```html
<!DOCTYPE html>
<html lang="en">
<head>
<meta charset="utf-8">
<title>Morvant Contracting – Business Card</title>
<link rel="stylesheet" href="https://fonts.googleapis.com/css2?family=Open+Sans:wght@400;600;700&display=swap">
<style>
  :root {
    --page: #ece9e4;
    --blue: #0f5ea3;
    --blue-light: #1a7ac4;
    --blue-dark: #0a4780;
    --white: #ffffff;
    --paper: #f3f3f3;
    --ink-blue: #14589a;
  }
  * { box-sizing: border-box; margin: 0; padding: 0; }
  html, body {
    width: 1200px; height: 1023px; overflow: hidden;
    background: var(--page);
    font-family: "Open Sans", sans-serif;
  }
  .canvas { position: relative; width: 1200px; height: 1023px; }
  .card {
    position: absolute; width: 700px; height: 400px;
    border-radius: 22px; overflow: hidden;
    box-shadow: 0 10px 28px rgba(0,0,0,.18);
  }
  /* Front */
  .card-front {
    left: 60px; top: 60px;
    background: radial-gradient(ellipse at 50% 38%, var(--blue-light) 0%, var(--blue) 55%, var(--blue-dark) 100%);
    color: var(--white);
    display: flex; flex-direction: column; align-items: center; justify-content: center;
  }
  .brand-mark { display: flex; align-items: center; gap: 14px; }
  .brand-dot { width: 18px; height: 18px; background: currentColor; flex: none; }
  .brand-name { font-weight: 700; font-size: 46px; letter-spacing: .5px; white-space: nowrap; }
  .website { margin-top: 26px; font-size: 18px; letter-spacing: 3px; }
  /* Back */
  .card-back { left: 440px; top: 560px; background: var(--paper); }
  .back-top {
    position: absolute; left: 0; top: 0; width: 100%; height: 185px;
    display: flex; align-items: center; justify-content: center;
    color: var(--ink-blue);
    background: linear-gradient(180deg, #ffffff, var(--paper));
  }
  .back-top .brand-name { font-size: 38px; }
  .back-top .brand-dot { width: 15px; height: 15px; }
  .back-band {
    position: absolute; left: 0; bottom: 0; width: 100%; height: 215px;
    background: linear-gradient(90deg, var(--blue-dark), var(--blue) 60%, var(--blue-light));
    color: var(--white);
    display: flex; justify-content: space-between; align-items: flex-start;
    padding: 22px 34px;
  }
  .contact-name { font-weight: 700; font-size: 22px; margin-bottom: 14px; }
  .contact-line { display: flex; align-items: center; gap: 10px; font-size: 15px; margin-bottom: 8px; }
  .contact-line svg { width: 16px; height: 16px; flex: none; }
  .services { text-align: right; font-size: 14px; line-height: 1.3; }
  .services-title {
    font-weight: 700; font-size: 14px; padding-bottom: 3px; margin-bottom: 6px;
    border-bottom: 1px solid var(--white); display: inline-block;
  }
  .services ul { margin: 0; }
  .services li { list-style: none; }
  .services li::after { content: " •"; }
</style>
</head>
<body>
<div class="canvas">
  <section class="card card-front">
    <div class="brand-mark">
      <span class="brand-dot"></span>
      <span class="brand-name">Morvant Contracting</span>
    </div>
    <p class="website">www.yourweb.com</p>
  </section>

  <section class="card card-back">
    <div class="back-top">
      <div class="brand-mark">
        <span class="brand-dot"></span>
        <span class="brand-name">Morvant Contracting</span>
      </div>
    </div>
    <div class="back-band">
      <div class="contact">
        <p class="contact-name">Your Name</p>
        <p class="contact-line">
          <svg viewBox="0 0 16 16" fill="none" stroke="#fff" stroke-width="1.4"><circle cx="8" cy="8" r="7"/><path d="M5.5 4.5l1.5 1.8-1 1a5 5 0 0 0 2.7 2.7l1-1 1.8 1.5-1 1.3c-3 0-6-3-6-6z" fill="#fff" stroke="none"/></svg>
          5074629183
        </p>
        <p class="contact-line">
          <svg viewBox="0 0 16 16" fill="none" stroke="#fff" stroke-width="1.4"><rect x="1" y="3" width="14" height="10"/><path d="M1 3l7 6 7-6"/></svg>
          morvantgc@quellmail.com
        </p>
      </div>
      <div class="services">
        <p class="services-title">We Offer</p>
        <ul>
          <li>Roofing</li>
          <li>Siding</li>
          <li>Gutter</li>
          <li>Additions</li>
          <li>Decks</li>
          <li>Handyman Services</li>
        </ul>
      </div>
    </div>
  </section>
</div>
</body>
</html>
```